Corvanto Card

The logo is the Spanish flag colors I want a vibrant eye catching design with the yellow / red colors over either Navy or white background or black even ,
Would like a 2D feel to the logo with another lighter color logo under it look ,

Contact Information for Business Card

Corvanto Flooring
Tobias Renwick
Main Number
Cell Number
Fax Number

Website on the side of the card somewhere

Font styles to use
Sans Serif

Colors
ec1f27
ffc214

Requirements
Must have
• 2 logos feel one is bolder and the other one underneath very light

```html
<!DOCTYPE html>
<html lang="en">
<head>
<meta charset="utf-8">
<title>Corvanto Flooring – Business Card</title>
<link rel="stylesheet" href="https://fonts.googleapis.com/css2?family=Archivo:wdth,wght@62..125,400;62..125,800;62..125,900&display=swap">
<style>
  :root {
    --brand-red: #ec1f27;
    --brand-yellow: #ffc214;
    --card-black: #1a1a1b;
    --stage: #0b0b0c;
    --ink-white: #f4f4f4;
    --rule-grey: #5a5a5a;
  }
  * { box-sizing: border-box; margin: 0; padding: 0; }
  html, body {
    width: 1200px; height: 900px; overflow: hidden;
    background: var(--stage);
    font-family: "Archivo", Arial, sans-serif;
  }
  .stage {
    width: 1200px; height: 900px;
    display: flex; flex-direction: column;
    align-items: center; justify-content: center; gap: 34px;
  }
  .card {
    position: relative;
    width: 700px; height: 400px;
    background: var(--card-black);
    overflow: hidden;
    box-shadow: 0 10px 30px rgba(0,0,0,.6);
  }
  .card__band {
    position: absolute; left: 0; right: 0; bottom: 0; height: 8px;
    background: linear-gradient(90deg, var(--brand-red) 0%, var(--brand-red) 40%, var(--brand-yellow) 60%, var(--brand-yellow) 100%);
  }

  /* Front */
  .card--front { display: flex; flex-direction: column; align-items: center; justify-content: center; }
  .brand { display: flex; align-items: center; gap: 18px; }
  .brand__square { width: 34px; height: 34px; background: var(--brand-red); border-radius: 4px; }
  .brand__name {
    color: var(--brand-red);
    font-weight: 900; font-stretch: 125%;
    font-size: 38px; line-height: 1.05; letter-spacing: 2px;
    text-transform: uppercase;
  }
  .website {
    margin-top: 54px;
    font-size: 19px; letter-spacing: 4px;
    color: var(--brand-yellow);
  }
  .website__edge { color: var(--brand-red); }

  /* Back */
  .card--back { padding: 96px 60px 0; }
  .person {
    text-align: center;
    font-weight: 900; font-stretch: 125%;
    font-size: 44px; letter-spacing: 2px; text-transform: uppercase;
  }
  .person__first { color: var(--brand-red); }
  .person__last { color: var(--brand-yellow); }
  .contacts {
    margin-top: 56px;
    display: flex; justify-content: center; align-items: center; gap: 30px;
    color: var(--ink-white); font-size: 21px;
  }
  .contacts__divider { width: 1px; height: 70px; background: var(--rule-grey); }
  .contacts__list { list-style: none; display: flex; flex-direction: column; gap: 10px; }
  .contacts__list--office { text-align: right; }
  .contacts__item { display: flex; align-items: center; gap: 10px; }
  .contacts__list--office .contacts__item { justify-content: flex-end; }
  .contacts__icon { width: 20px; height: 20px; flex: none; }
  .contacts__icon--red { fill: var(--brand-red); }
  .contacts__icon--yellow { fill: var(--brand-yellow); }
</style>
</head>
<body>
<main class="stage">
  <section class="card card--front" aria-label="Card front">
    <div class="brand">
      <span class="brand__square"></span>
      <h1 class="brand__name">Corvanto Flooring</h1>
    </div>
    <p class="website"><span class="website__edge">www.</span>corvantofloors<span class="website__edge">.com</span></p>
    <div class="card__band"></div>
  </section>

  <section class="card card--back" aria-label="Card back">
    <h2 class="person"><span class="person__first">Tobias</span> <span class="person__last">Renwick</span></h2>
    <div class="contacts">
      <ul class="contacts__list contacts__list--office">
        <li class="contacts__item">555 210 0147
          <svg class="contacts__icon contacts__icon--red" viewBox="0 0 20 20" aria-label="Fax"><rect x="5" y="2" width="10" height="5"/><rect x="2" y="7" width="16" height="8" rx="2"/><rect x="5" y="12" width="10" height="6" fill="#1a1a1b"/><rect x="6" y="13" width="8" height="4"/></svg>
        </li>
        <li class="contacts__item">hello@corvanto.com
          <svg class="contacts__icon contacts__icon--red" viewBox="0 0 20 20" aria-label="Email"><rect x="1" y="4" width="18" height="12" rx="1"/><path d="M2 5l8 6 8-6" stroke="#1a1a1b" stroke-width="1.6" fill="none"/></svg>
        </li>
      </ul>
      <span class="contacts__divider"></span>
      <ul class="contacts__list">
        <li class="contacts__item">
          <svg class="contacts__icon contacts__icon--yellow" viewBox="0 0 20 20" aria-label="Main number"><path d="M2 8c0-3 4-5 8-5s8 2 8 5l-4 1-1-2c-2-.5-4-.5-6 0L6 9z"/><path d="M5 10h10l2 7H3z"/></svg>
          555 318 2240
        </li>
        <li class="contacts__item">
          <svg class="contacts__icon contacts__icon--yellow" viewBox="0 0 20 20" aria-label="Cell number"><path d="M6 1h8a2 2 0 0 1 2 2v14a2 2 0 0 1-2 2H6a2 2 0 0 1-2-2V3a2 2 0 0 1 2-2zm0 3v11h8V4z"/></svg>
          555 402 7716
        </li>
      </ul>
    </div>
    <div class="card__band"></div>
  </section>
</main>
</body>
</html>
```